Website for legal expungement services with button to qualify/disqualify potential clients

Larkfield Record Relief, LLC is a law firm focusing in legal expungement servcies (allowing people to erase criminal court records, police records, proseution files, etc). I want a more modern look which exudes confidence in the services. I am looking for a clean website that looks very polished. I want to keep the pages to a minimum, as I want the page not so much to answer questions, but to direct traffic to contact the law office. I would like the main focus point to be an button which would take a client through a series of questions to see if they would qualify for the services; this serves two purposes 1) to collect contact info for future marketing via email and 2) eliminate individuals who we are currently unable to help. A current theme that I have played around with are "Change so much, you'll need to reintroduce yourself" alongside a picture of a guys hand outstretched.
On the landing page, I would like a very brief and to the point explanation of what the service would be (i.e. "Leave your past in the past; expunge all your criminal records" ), followed by a list of benefits that it provides. (NB: included is a file "law post card-02" that includes the main benefits to expungement). Also included are two logo files for a more updated logo I currently use ("LRR Logo" and LRR Logo2") (NB: I'm open to revisions on this as well). Lastly, I've had two very minor 'ads' that I did ("postcard back" and "HVC Ad") that I like the idea of.

Target Market(s)

Middle/upper-middle class, mostly male, people with a criminal record or criminal accusation

Industry/Entity Type

Legal Services

Coding

Coded - Design and coding required

Requirements
Must have
• Button that attracts attention up front (possibly stand out coloring) to click to open up a series of questions to qualify/eliminate prospects, and simultaneously gather their info. Also, must be mobile friendly.

```html
<!DOCTYPE html>
<html lang="en">
<head>
<meta charset="utf-8">
<title>Larkfield Record Relief</title>
<link href="https://fonts.googleapis.com/css2?family=Roboto:wght@300;400;500;700&display=swap" rel="stylesheet">
<style>
:root{
  --navy:#003b7a;
  --gold:#d3a030;
  --ink:#222;
  --footer:#141414;
  --white:#fff;
}
*{box-sizing:border-box;margin:0;padding:0}
html,body{width:1200px;height:3306px;overflow:hidden}
body{position:relative;font-family:'Roboto',sans-serif;color:var(--ink);background:var(--white)}
.abs{position:absolute}
.center{left:0;width:1200px;text-align:center}

/* header */
.site-header{position:absolute;left:0;top:0;width:1200px;height:110px;background:var(--white)}
.brand{position:absolute;left:88px;top:38px;display:flex;align-items:center;gap:12px}
.brand-square{width:22px;height:22px;background:var(--navy)}
.brand-name{font-size:19px;font-weight:500;color:var(--navy)}
.top-contact{position:absolute;top:29px;font-size:13px;color:#555;display:flex;align-items:center;gap:8px}
.main-nav{position:absolute;top:68px;left:550px;display:flex;font-size:13px}
.main-nav a{text-decoration:none;color:#222;margin-right:38px}
.main-nav a.active{color:var(--gold)}
.btn-book{position:absolute;left:966px;top:25px;width:146px;height:61px;border:2px solid var(--navy);color:var(--navy);font-size:13px;font-weight:500;text-align:center;line-height:19px;padding-top:10px}

/* hero */
.hero-photo{position:absolute;left:0;top:110px;width:1200px;height:580px;background:linear-gradient(100deg,#7a6f60 0%,#4a433a 30%,#6b5638 52%,#c08a2e 68%,#d69c34 74%,#6e6252 92%,#8a8278 100%)}
.hero-shape{position:absolute;left:0;top:540px}
.hero-title{top:278px;font-size:37px;font-weight:700;color:var(--white);line-height:44px;letter-spacing:.3px}
.btn-consult{position:absolute;left:523px;top:435px;width:153px;height:36px;background:var(--gold);border:2px solid #f3d58a;color:var(--white);font-size:14px;line-height:32px;text-align:center}
.dots{position:absolute;top:591px;left:564px;display:flex;gap:15px}
.dots span{width:14px;height:14px;border:2px solid var(--white);border-radius:50%}
.dots span.on{border-color:var(--gold);background:radial-gradient(var(--gold) 30%,transparent 35%)}

/* welcome */
.eyebrow{font-size:17px;color:var(--gold)}
.welcome-title{top:788px;font-size:29px;color:var(--navy);font-weight:400}
.welcome-text{position:absolute;left:226px;width:748px;top:843px;font-size:14px;line-height:22.5px;text-align:center;color:#222}

/* services */
.services{position:absolute;left:0;top:984px;width:1200px;height:657px;background:var(--navy)}
.section-title{font-size:37px;font-weight:700}
.service-card{position:absolute;top:1161px;width:316px;height:321px;border:3px solid #1a2e4a;overflow:hidden}
.service-card .photo{position:absolute;inset:0}
.service-card .label{position:absolute;left:0;right:0;bottom:18px;text-align:center;color:var(--white);font-size:17px;line-height:22px}
.service-card.active{border-color:#c9d1dc}
.drag{position:absolute;left:1079px;top:1291px;width:64px;height:64px;border-radius:50%;background:var(--white);text-align:center;font-size:10px;color:#222;padding-top:14px}
.btn-outline{position:absolute;border:2px solid #1f5aa0;color:var(--white);font-size:14px;text-align:center}

/* benefits */
.benefit-title{top:1741px;font-size:37px;font-weight:700;color:var(--navy)}
.benefit-photo{position:absolute;left:462px;top:1823px;width:296px;height:367px;border:3px solid #e6e6e6;background:linear-gradient(160deg,#9a9a9a,#4a4a4a 40%,#2e2e2e 60%,#777 100%)}
.benefit-photo .name{position:absolute;left:0;right:0;top:168px;text-align:center;color:var(--white);font-size:22px;font-weight:500}
.benefit{position:absolute;font-size:15px;line-height:22.5px;color:#222;width:180px}
.benefit.right{width:220px;text-align:right}
.benefit-icon{position:absolute;width:74px;height:74px;border-radius:50%;background:var(--gold);border:3px solid #f1dca6;box-shadow:0 0 0 2px var(--gold);display:flex;align-items:center;justify-content:center}
.benefit-icon svg{width:40px;height:40px;fill:none;stroke:#fff;stroke-width:2;stroke-linejoin:round;stroke-linecap:round}

/* consult */
.consult{position:absolute;left:0;top:2272px;width:1200px;height:700px;background:linear-gradient(90deg,#f4f4f4 0%,#efefef 55%,#d8d3cb 78%,#b9b2a6 100%)}
.consult-title{top:2342px;font-size:37px;font-weight:700;color:var(--navy)}
.field{position:absolute;background:var(--white);border:1px solid #dcdcdc;font-size:13px;color:#9a9a9a;padding-left:42px;display:flex;align-items:center}
.field svg{position:absolute;left:16px}
.field.area{align-items:flex-start;padding-top:14px}
.btn-solid{position:absolute;background:var(--navy);border:2px solid var(--white);outline:2px solid var(--navy);color:var(--white);font-size:15px;text-align:center}

/* footer */
.footer-shape{position:absolute;left:0;top:2760px}
.footer{position:absolute;left:0;top:2900px;width:1200px;height:366px;background:var(--footer)}
.footer-brand{position:absolute;left:0;width:1200px;top:2895px;display:flex;justify-content:center;align-items:center;gap:16px}
.footer-brand .brand-square{width:28px;height:28px;background:var(--white)}
.footer-brand .brand-name{color:var(--white);font-size:28px}
.footer-heading{position:absolute;top:3008px;font-size:19px;font-weight:700;color:var(--gold)}
.footer-item{position:absolute;color:var(--white);font-size:14px;display:flex;align-items:flex-start;gap:14px;line-height:19px}
.footer-link{position:absolute;left:431px;color:var(--white);font-size:15px}
.news-field{position:absolute;left:657px;width:318px;height:36px;border:1px solid #5a5a5a;color:#888;font-size:14px;padding-left:20px;line-height:34px}
.social{position:absolute;left:1075px;width:34px;height:34px;border:1.5px solid var(--white);border-radius:50%;color:var(--white);font-size:8px;text-align:center;line-height:31px}
.social.on{background:var(--gold);border-color:var(--gold)}
.bottom-bar{position:absolute;left:0;top:3266px;width:1200px;height:40px;background:var(--navy);color:var(--white);font-size:13px;text-align:center;line-height:40px}
</style>
</head>
<body>

<header class="site-header">
  <div class="brand">
    <span class="brand-square"></span>
    <span class="brand-name">Larkfield Record Relief</span>
  </div>
  <div class="top-contact" style="left:695px">
    <svg width="13" height="13" viewBox="0 0 24 24"><path fill="#d3a030" d="M6.6 10.8a15 15 0 0 0 6.6 6.6l2.2-2.2c.3-.3.7-.4 1-.2 1.1.4 2.3.6 3.6.6.6 0 1 .4 1 1V20c0 .6-.4 1-1 1A17 17 0 0 1 3 4c0-.6.4-1 1-1h3.5c.6 0 1 .4 1 1 0 1.3.2 2.5.6 3.6.1.3 0 .7-.2 1z"/></svg>
    123-456-7890
  </div>
  <div class="top-contact" style="left:821px">
    <svg width="14" height="12" viewBox="0 0 24 20"><rect x="1" y="4" width="22" height="15" rx="2" fill="#d3a030"/><path d="M1 6l11 7 11-7" stroke="#fff" stroke-width="2" fill="none"/></svg>
    info@lrr.com
  </div>
  <nav class="main-nav">
    <a class="active" href="#">-- HOME --</a>
    <a href="#">ABOUT US</a>
    <a href="#">SERVICES</a>
    <a href="#">CONTACT US</a>
  </nav>
  <div class="btn-book">BOOK AN<br>APPOINTMENT</div>
</header>

<section>
  <div class="hero-photo" role="img" aria-label="Lawyer signing documents at a desk beside brass scales of justice, warm window light"></div>
  <svg class="hero-shape" width="1200" height="160" viewBox="0 0 1200 160">
    <path d="M0 18 L0 160 L1200 160 L1200 18 L600 130 Z" fill="#fff"/>
    <path d="M333 89 L600 149 L867 89 L600 127 Z" fill="#003b7a"/>
  </svg>
  <h1 class="abs center hero-title">CHANGE SO MUCH...<br>YOU'LL NEED TO REINTRODUCE<br>YOURSELF.</h1>
  <div class="btn-consult">CONSULT NOW</div>
  <div class="dots"><span></span><span class="on"></span><span></span></div>
</section>

<section>
  <p class="abs center eyebrow" style="top:767px">Welcome to</p>
  <h2 class="abs center welcome-title">LARKFIELD RECORD RELIEF</h2>
  <p class="welcome-text">is 5-star rated firm, which has been formed with the passing of the Record Relief Act of 2020. It is a subdivision of the Hollins Law Firm, and since its creation has helped over 100 local citizens successfully expunge their criminal records.</p>
</section>

<section class="services"></section>
<p class="abs center" style="top:1067px;font-size:15px;color:var(--gold)">What we do</p>
<h2 class="abs center section-title" style="top:1086px;color:#fff">SERVICES</h2>

<div class="service-card" style="left:88px">
  <div class="photo" role="img" aria-label="Hand holding a pen over a criminal records form beside a calculator" style="background:linear-gradient(180deg,#7a736a 0%,#5e5a55 30%,#3a3a3c 60%,#0f1218 100%)"></div>
  <div class="label">CRIMINAL RECORD<br>EXPUNGEMENTS</div>
</div>
<div class="service-card" style="left:443px">
  <div class="photo" role="img" aria-label="Worried woman sitting among moving boxes" style="background:linear-gradient(180deg,#8d7560 0%,#6e5a48 35%,#3a3430 65%,#111 100%)"></div>
  <div class="label">EVICTION<br>EXPUNGEMENTS</div>
</div>
<div class="service-card active" style="left:796px">
  <div class="photo" role="img" aria-label="Two men in suits talking in an office" style="background:linear-gradient(180deg,#8a7a6c 0%,#5f5650 40%,#b08a3a 70%,#d6a82e 100%)"></div>
  <div class="label">EVICTION LEGAL<br>DEFENSE</div>
</div>
<div class="drag">
  <svg width="18" height="14" viewBox="0 0 18 14"><path d="M1 7h15M10 1l6 6-6 6" stroke="#222" stroke-width="1.6" fill="none"/></svg><br>DRAG
</div>
<div class="btn-outline" style="left:544px;top:1525px;width:112px;height:34px;line-height:30px">VIEW ALL</div>

<section>
  <p class="abs center" style="top:1718px;font-size:15px;color:var(--gold)">The Benefits of</p>
  <h2 class="abs center benefit-title">EXPUNGEMENT</h2>
  <div class="benefit-photo" role="img" aria-label="Black and white photo of scales of justice on a lawyer's desk"><div class="name">Larkfield Record Relief</div></div>

  <div class="benefit-icon" style="left:112px;top:1822px"><svg viewBox="0 0 40 40"><rect x="5" y="13" width="30" height="20" rx="2"/><path d="M15 13v-4h10v4M5 21h30"/></svg></div>
  <p class="benefit" style="left:199px;top:1826px">More and better job opportunities leading to higher income</p>
  <div class="benefit-icon" style="left:112px;top:1921px"><svg viewBox="0 0 40 40"><path d="M10 5h15l6 6v24H10z"/><path d="M14 16h12M14 22h12M14 28h8"/></svg></div>
  <p class="benefit" style="left:199px;top:1936px">Loan qualification and better loan rates</p>
  <div class="benefit-icon" style="left:112px;top:2020px"><svg viewBox="0 0 40 40"><path d="M20 4l13 5v10c0 8-6 14-13 17C13 33 7 27 7 19V9z"/><path d="M14 20l4 4 8-8"/></svg></div>
  <p class="benefit" style="left:199px;top:2035px">Protecting your<br>privacy</p>
  <div class="benefit-icon" style="left:112px;top:2120px"><svg viewBox="0 0 40 40"><path d="M4 15l16-7 16 7-16 7z"/><path d="M11 18v8c3 3 15 3 18 0v-8M36 15v9"/></svg></div>
  <p class="benefit" style="left:199px;top:2134px">Better education<br>opportunities</p>

  <div class="benefit-icon" style="left:1013px;top:1822px"><svg viewBox="0 0 40 40"><rect x="5" y="9" width="30" height="22" rx="2"/><circle cx="14" cy="19" r="4"/><path d="M22 16h9M22 22h9M9 27h8"/></svg></div>
  <p class="benefit right" style="left:777px;top:1835px">Removing the stigma of<br>having a criminal record</p>
  <div class="benefit-icon" style="left:1013px;top:1921px"><svg viewBox="0 0 40 40"><path d="M5 19L20 7l15 12"/><path d="M9 16v18h22V16"/><path d="M17 34v-9h6v9"/></svg></div>
  <p class="benefit right" style="left:777px;top:1936px">More options for<br>housing</p>
  <div class="benefit-icon" style="left:1013px;top:2020px"><svg viewBox="0 0 40 40"><path d="M5 14l15-8 15 8z"/><path d="M9 17v13M16 17v13M24 17v13M31 17v13M5 33h30"/></svg></div>
  <p class="benefit right" style="left:777px;top:2035px">Qualifying for government<br>assistance programs</p>
  <div class="benefit-icon" style="left:1013px;top:2120px"><svg viewBox="0 0 40 40"><rect x="9" y="7" width="22" height="28" rx="2"/><path d="M16 5h8v5h-8zM14 18l2 2 4-4M23 18h4M14 27l2 2 4-4M23 27h4"/></svg></div>
  <p class="benefit right" style="left:777px;top:2134px">Lower insurance<br>premiums</p>
</section>

<section class="consult" role="img" aria-label="Faded bronze statue of Lady Justice on a light background"></section>
<h2 class="abs center consult-title">CONSULT NOW</h2>
<div class="field" style="left:303px;top:2420px;width:287px;height:37px">
  <svg width="13" height="14" viewBox="0 0 14 16"><circle cx="7" cy="4.5" r="3.5" fill="none" stroke="#777" stroke-width="1.4"/><path d="M1 15c0-4 3-6 6-6s6 2 6 6" fill="none" stroke="#777" stroke-width="1.4"/></svg>First Name</div>
<div class="field" style="left:608px;top:2420px;width:288px;height:37px">
  <svg width="13" height="14" viewBox="0 0 14 16"><circle cx="7" cy="4.5" r="3.5" fill="none" stroke="#777" stroke-width="1.4"/><path d="M1 15c0-4 3-6 6-6s6 2 6 6" fill="none" stroke="#777" stroke-width="1.4"/></svg>Last Name</div>
<div class="field" style="left:303px;top:2470px;width:287px;height:37px">
  <svg width="14" height="11" viewBox="0 0 14 11"><rect x=".7" y=".7" width="12.6" height="9.6" rx="1" fill="none" stroke="#777" stroke-width="1.3"/><path d="M1 1l6 5 6-5" fill="none" stroke="#777" stroke-width="1.3"/></svg>Email</div>
<div class="field" style="left:608px;top:2470px;width:288px;height:37px">
  <svg width="10" height="14" viewBox="0 0 10 14"><rect x=".7" y=".7" width="8.6" height="12.6" rx="1.5" fill="none" stroke="#777" stroke-width="1.3"/></svg>Phone</div>
<div class="field area" style="left:303px;top:2521px;width:593px;height:94px">
  <svg width="13" height="13" viewBox="0 0 13 13" style="top:16px"><path d="M.7.7h11.6v8l-3.6 3.6H.7z" fill="none" stroke="#777" stroke-width="1.3"/></svg>How can we help?</div>
<div class="btn-solid" style="left:548px;top:2657px;width:104px;height:37px;line-height:33px">SUBMIT</div>

<svg class="footer-shape" width="1200" height="145" viewBox="0 0 1200 145">
  <path d="M0 144 L600 15 L1200 144 L1200 145 L0 145 Z" fill="#141414"/>
  <path d="M333 80 L600 13 L867 80 L600 27 Z" fill="#003b7a"/>
  <path d="M0 144 L600 15 L1200 144" fill="none" stroke="#fff" stroke-width="4"/>
</svg>
<footer class="footer"></footer>
<div class="footer-brand">
  <span class="brand-square"></span>
  <span class="brand-name">Larkfield Record Relief</span>
</div>

<h3 class="footer-heading" style="left:88px">CONTACT US</h3>
<div class="footer-item" style="left:88px;top:3053px;font-size:22px;line-height:26px;align-items:center">
  <svg width="16" height="16" viewBox="0 0 24 24"><path fill="#d3a030" d="M6.6 10.8a15 15 0 0 0 6.6 6.6l2.2-2.2c.3-.3.7-.4 1-.2 1.1.4 2.3.6 3.6.6.6 0 1 .4 1 1V20c0 .6-.4 1-1 1A17 17 0 0 1 3 4c0-.6.4-1 1-1h3.5c.6 0 1 .4 1 1 0 1.3.2 2.5.6 3.6.1.3 0 .7-.2 1z"/></svg>123-456-7890</div>
<div class="footer-item" style="left:88px;top:3098px;align-items:center">
  <svg width="15" height="12" viewBox="0 0 24 20"><rect x="1" y="4" width="22" height="15" rx="2" fill="#d3a030"/><path d="M1 6l11 7 11-7" stroke="#141414" stroke-width="2" fill="none"/></svg>info@lrr.com</div>
<div class="footer-item" style="left:88px;top:3140px">
  <svg width="15" height="18" viewBox="0 0 14 18"><path d="M7 0a7 7 0 0 0-7 7c0 5 7 11 7 11s7-6 7-11a7 7 0 0 0-7-7z" fill="#d3a030"/><circle cx="7" cy="7" r="2.5" fill="#141414"/></svg>
  <span>4410 Birchwood Lane, Suite 320 -<br>Larkfield, LK - 2930</span></div>

<h3 class="footer-heading" style="left:431px">QUICK LINKS</h3>
<a class="footer-link" style="top:3053px;color:var(--gold);text-decoration:underline">Home</a>
<a class="footer-link" style="top:3088px">About Us</a>
<a class="footer-link" style="top:3125px">Services</a>
<a class="footer-link" style="top:3162px">Contact Us</a>

<h3 class="footer-heading" style="left:656px">NEWSLETTER</h3>
<div class="news-field" style="top:3057px">Your Name</div>
<div class="news-field" style="top:3109px">Your Email</div>
<div class="btn-solid" style="left:658px;top:3164px;width:103px;height:36px;line-height:32px;border-color:#141414">SUBMIT</div>

<div class="social" style="top:3047px">Page</div>
<div class="social on" style="top:3089px">Feed</div>
<div class="social" style="top:3133px">Net</div>
<svg class="abs" style="left:1149px;top:3217px" width="20" height="24" viewBox="0 0 20 24"><path d="M10 0L20 24 10 18 0 24z" fill="#fff"/></svg>

<div class="bottom-bar">© 2023 Larkfield Record Relief. All Right Reserved &nbsp;&nbsp;&nbsp;&nbsp;&nbsp;&nbsp;&nbsp;&nbsp;&nbsp;&nbsp; Terms and Conditions &nbsp;&nbsp;&nbsp; | &nbsp;&nbsp;&nbsp; Privacy Policy</div>

</body>
</html>
```